Email Signature & Facebook Cover Design – Brightpath Learning Nook

I’m looking for a clean, professional email signature and a matching Facebook cover photo for my tutoring business, Brightpath Learning Nook.
The email signature needs to display properly across Outlook and iPhone without the image appearing as an attachment. It should include my logo and contact details and have a friendly but professional look suitable for an education business.
Details to include:
Dana Morrow
Director & Lead Tutor
Brightpath Learning Nook
hello@brightpathlearningnook.co.uk
www.brightpathlearningnook.co.uk
01632 960418
The Facebook cover should match the branding, feel professional and welcoming, and be optimised for desktop and mobile.

```html
<!DOCTYPE html>
<html lang="en">
<head>
<meta charset="utf-8">
<title>HTML Email Signature – Brightpath Learning Nook</title>
<link rel="stylesheet" href="https://fonts.googleapis.com/css2?family=Montserrat:wght@400;600;700&family=Source+Serif+4:wght@400&family=Caveat+Brush&display=swap">
<style>
  :root {
    --brand-green: #45b96b;
    --brand-green-deep: #3faa60;
    --ink: #4a4a4a;
    --white: #ffffff;
    --photo-warm: #b97a45;
    --photo-light: #d9b99a;
  }
  * { margin: 0; padding: 0; box-sizing: border-box; }
  html, body { width: 1200px; height: 1200px; overflow: hidden; background: var(--white); }
  .canvas { position: relative; width: 1200px; height: 1200px; background: var(--white); font-family: "Montserrat", sans-serif; }

  .heading {
    position: absolute; top: 314px; left: 0; width: 1200px; text-align: center;
    font-weight: 700; font-size: 33px; letter-spacing: 1px; color: var(--brand-green);
  }

  .brand-mark {
    position: absolute; left: 293px; top: 427px; width: 200px; height: 200px; border-radius: 50%;
    background: var(--brand-green);
    display: flex; align-items: center; justify-content: center; text-align: center;
  }
  .brand-mark__name {
    font-family: "Montserrat", sans-serif; font-weight: 700; font-size: 22px; line-height: 1.2;
    color: var(--white); padding: 0 26px;
  }

  .divider { position: absolute; left: 523px; top: 417px; width: 2px; height: 221px; background: var(--brand-green); }

  .details { position: absolute; left: 555px; top: 417px; color: var(--ink); }
  .details__name { font-weight: 600; font-size: 23px; line-height: 27px; color: var(--brand-green); letter-spacing: 0.2px; }
  .details__role { font-size: 22px; line-height: 27px; font-weight: 400; }

  .contact { position: absolute; left: 555px; top: 512px; list-style: none; }
  .contact__item { display: flex; align-items: center; height: 30px; font-size: 22px; color: var(--ink); }
  .contact__icon { width: 22px; height: 22px; margin-right: 10px; flex: none; }

  .social { position: absolute; left: 554px; top: 612px; display: flex; gap: 5px; }
  .social__dot { width: 25px; height: 25px; border-radius: 50%; background: var(--brand-green); }

  .banner {
    position: absolute; left: 294px; top: 669px; width: 598px; height: 113px; background: var(--brand-green);
  }
  .banner__tagline {
    position: absolute; left: 30px; top: 16px; color: var(--white);
    font-family: "Source Serif 4", serif; font-size: 30px; line-height: 36px; font-weight: 400;
  }
  .banner__accent { font-family: "Caveat Brush", cursive; font-size: 30px; }

  .banner-photo {
    position: absolute; left: 758px; top: 623px; width: 138px; height: 159px;
    border-radius: 60px 60px 0 0;
    background: linear-gradient(160deg, var(--photo-light) 0%, var(--photo-warm) 70%);
  }
</style>
</head>
<body>
<main class="canvas">
  <h1 class="heading">HTML EMAIL SIGNATURE</h1>

  <div class="brand-mark">
    <span class="brand-mark__name">Brightpath Learning Nook</span>
  </div>

  <div class="divider"></div>

  <div class="details">
    <p class="details__name">DANA MORROW</p>
    <p class="details__role">Director &amp; Lead Tutor</p>
    <p class="details__role">Brightpath Learning Nook</p>
  </div>

  <ul class="contact">
    <li class="contact__item">
      <svg class="contact__icon" viewBox="0 0 24 24" aria-hidden="true">
        <path d="M2 8c0-3 4-5 10-5s10 2 10 5v2h-5V7.5c-1.5-.6-3-.8-5-.8s-3.5.2-5 .8V10H2z" fill="#45b96b"/>
        <path d="M5 12l2-3h10l2 3v9H5z" fill="#45b96b"/>
        <circle cx="12" cy="16" r="3" fill="#fff"/>
      </svg>
      01632 960418
    </li>
    <li class="contact__item">
      <svg class="contact__icon" viewBox="0 0 24 24" aria-hidden="true">
        <rect x="1" y="5" width="22" height="14" fill="#45b96b"/>
        <path d="M1 6l11 7 11-7" fill="none" stroke="#fff" stroke-width="1.6"/>
      </svg>
      hello@brightpathlearningnook.co.uk
    </li>
    <li class="contact__item">
      <svg class="contact__icon" viewBox="0 0 24 24" aria-hidden="true">
        <circle cx="12" cy="12" r="10.5" fill="#45b96b"/>
        <path d="M7 5c3 1 2 4 5 5s1 4-1 5-1 4-2 5M15 3c-1 3 2 3 3 5s-1 3 1 5" fill="none" stroke="#fff" stroke-width="1.4"/>
      </svg>
      www.brightpathlearningnook.co.uk
    </li>
  </ul>

  <div class="social" aria-label="Social links">
    <span class="social__dot"></span>
    <span class="social__dot"></span>
    <span class="social__dot"></span>
    <span class="social__dot"></span>
  </div>

  <section class="banner">
    <p class="banner__tagline">Learning that<br>clicks, <span class="banner__accent">confidence</span> that truly sticks.</p>
  </section>

  <div class="banner-photo" role="img" aria-label="Photo of a smiling student holding an open laptop"></div>
</main>
</body>
</html>
```